Banner Ad Design Project

I need a banner design. The website is under construction at www.brightmarrow.example

Name: Bright Marrow
Tagline: Steady Sparks for crowded calendars

This is a leadership development and executive coaching site. The past site is live at www.quillstepnow.example. (so you can get a sense of the content)

The audience are (BUSY) executives, senior managers, leaders and top professionals, so the feel needs to be highly professional but also modern and fresh. I want to communicate energy but also solid and trust worthy and not too new agey. The audience are also people with strong social values who want to change things - so not too corporate (Ie suits!)

I would like the design to be floating on a white background, very clean and simple. I am attracted to reds or sunset (burn orange crimson colors.) But totally open to any color ideas.
I am giving an open brief for your ideas.
Here are the dimensions 960px wide, roughly 190px height.

Reason: The weekend might give more time to designers to get involved. Thanks Vina

Hi designers

You may not have seen the additions I gave to this brief.

The banner should not have leader out front photo's. Maybe less corporate than I initially thought. 
Not too corporate (no suits!) Please no chess pieces, jigsaw pieces, cartoon images, cliche leadership images. 
Am am trying for inspiration /inspiring whilst still being professional. Very simple and clean.
Please can the design be floating in a white background so that the web page is borderless - A bit like it is in http://palmoriskel.example/
Thank you

Target Market(s)

Senior managers, executives but people who also want to change the world!

Industry/Entity Type

Construction

Requirements
Should not have
• Should not have leader out front photo's.
Maybe less corporate than I initially thought.
Am am trying for inspiration /inspiring whilst still being professional.
Please no chess pieces, jigsaw pieces, cartoon images, cliche leadership images. Not too corporate (Ie suits!)

Thanks

```html
<!DOCTYPE html>
<html lang="en">
<head>
<meta charset="utf-8">
<title>Bright Marrow — Banner</title>
<link rel="stylesheet" href="https://fonts.googleapis.com/css2?family=Ultra&family=Poiret+One&display=swap">
<style>
  :root {
    --photo-crimson: #b3300c;
    --photo-orange: #e0701a;
    --photo-amber: #f0a232;
    --text-white: #ffffff;
    --title-glow: rgba(255, 245, 220, 0.85);
    --text-shade: rgba(110, 40, 0, 0.35);
  }
  html, body {
    margin: 0;
    padding: 0;
    overflow: hidden;
    background: #ffffff;
  }
  .banner {
    position: relative;
    width: 1200px;
    height: 238px;
    overflow: hidden;
  }
  .banner__photo {
    position: absolute;
    inset: 0;
    background: linear-gradient(180deg, var(--photo-crimson) 0%, var(--photo-orange) 50%, var(--photo-amber) 100%);
  }
  .banner__title {
    position: absolute;
    left: 0;
    right: 0;
    top: 50px;
    margin: 0;
    text-align: center;
    font-family: "Ultra", serif;
    font-weight: 400;
    font-size: 80px;
    line-height: 1;
    letter-spacing: 1px;
    word-spacing: 60px;
    white-space: nowrap;
    color: var(--text-white);
    text-shadow: 0 0 6px var(--title-glow), 2px 3px 4px var(--text-shade);
  }
  .banner__tagline {
    position: absolute;
    left: 0;
    right: 0;
    top: 160px;
    margin: 0;
    text-align: center;
    font-family: "Poiret One", sans-serif;
    font-weight: 400;
    font-size: 42px;
    line-height: 1;
    white-space: nowrap;
    color: var(--text-white);
    text-shadow: 0 0 3px var(--text-shade);
  }
</style>
</head>
<body>
  <header class="banner">
    <div class="banner__photo" role="img" aria-label="Photograph of a fiery orange and crimson sunset sky over the sea"></div>
    <h1 class="banner__title">Bright Marrow</h1>
    <p class="banner__tagline">Steady Sparks for crowded calendars</p>
  </header>
</body>
</html>
```